Saveurs Du Matin

looking fo an e-commerce site something that will stand out the site domain will be saveursdumatin.example need somthing bold and refind as well; eye appealing and not too cartonish please visit our competetors to see waht we are going for they are (zestlyne.example, brantaro4u.example and quellabrookfarms.example) this site should have multiple pages mainly looking for a layout to start the site and code.

PLEASE REMEMBER WE REQUIRE THE CODE....

Target Market(s)

anyone who loves food or is fasinated by it

Industry/Entity Type

E-Commerce

Requirements
Must have
• .an easy to work site that makes sense and that is not all over the place it should have in the navigation feature: Olive oils, Balsamic Vinegars, Misc. Vinegars and oils, Specialty salts, organic spices, Specialty Spices, Kitchen Tools. also pleas use our logo in the design i have attached below
Nice to have
• clean and some spices, salt, pepermills, morter and pistels, olive oils, trying to stick to a clean presentation
Should not have
• no cartoon figures or alike, anything too playfull

```html
<!DOCTYPE html>
<html lang="en">
<head>
<meta charset="utf-8">
<title>Saveurs Du Matin – Highest Quality Spices</title>
<link href="https://fonts.googleapis.com/css2?family=Noto+Sans:wght@300;400;700&family=Arimo:wght@400;700&display=swap" rel="stylesheet">
<style>
:root{
  --dark:#2f2f2f;
  --dark-2:#383838;
  --rule:#585858;
  --brown:#8e4a1c;
  --brown-mid:#a9602c;
  --brown-light:#c88350;
  --tab:#e6ae80;
  --grey-panel:#eeeeee;
  --grey-item:#e0e0e0;
  --text:#333333;
  --muted:#555555;
  --accent-text:#8a4a18;
  --orange:#f2a23a;
  --red:#e5251f;
  --white:#ffffff;
}
*{box-sizing:border-box;margin:0;padding:0}
html,body{width:1200px;height:1150px;overflow:hidden}
body{position:relative;background:var(--white);font-family:"Arimo",Arial,sans-serif;color:var(--text)}
a{color:inherit;text-decoration:none}
.abs{position:absolute}

/* header */
.topbar{left:0;top:0;width:1200px;height:66px;background:var(--dark)}
.topbar-rule{left:0;top:66px;width:1200px;height:4px;background:var(--rule)}
.subbar{left:0;top:70px;width:1200px;height:46px;background:var(--dark-2)}
.account-links{left:109px;top:13px;font-family:"Noto Sans",sans-serif;font-size:11.5px;color:#e8e8e8}
.account-links span{margin:0 8px;color:#bbb}
.search{left:643px;top:23px;width:183px;height:25px;background:var(--white);border:1px solid #999}
.search span{position:absolute;left:7px;top:4px;font-size:12px;color:#999;font-family:"Noto Sans",sans-serif}
.search svg{position:absolute;right:4px;top:3px}
.phone{right:112px;top:10px;font-family:"Noto Sans",sans-serif;font-size:25px;color:var(--white);letter-spacing:1.5px}
.hours{right:112px;top:43px;font-family:"Noto Sans",sans-serif;font-size:12px;color:#eee;letter-spacing:.3px}
.brand-slot{left:114px;top:49px;width:219px;height:67px;background:#f0f0f0}
.cart{left:915px;top:83px;font-family:"Noto Sans",sans-serif;font-size:12px;color:#ddd}
.cart b{color:var(--orange);font-weight:700}
.cart svg{vertical-align:middle;margin-right:8px}

/* navigation */
.navband{left:0;top:116px;width:1200px;height:40px;background:linear-gradient(var(--brown-light),var(--brown-mid) 45%,var(--brown))}
.navline{left:102px;width:996px;border-top:1px dotted #f0c9a5}
.mainnav{right:104px;top:120px;height:32px;display:flex;font-family:"Noto Sans",sans-serif;font-size:12.5px;color:var(--white)}
.mainnav a{padding:0 16px;line-height:31px;border-left:1px solid #c47b47}
.mainnav a:first-child{border-left:0}
.mainnav a.active{background:var(--tab);color:#3a1d08}

/* left column */
.logo-area{left:114px;top:156px;width:219px;height:196px;background:#fafafa;text-align:center}
.logo-area .mark{display:block;margin:40px auto 0;width:70px;height:70px;background:#e9e0d8}
.logo-area .name{display:block;margin-top:26px;font-family:"Noto Sans",sans-serif;font-size:20px;color:var(--accent-text)}
.section-head{left:103px;width:230px;height:40px;background:linear-gradient(var(--brown-light),var(--brown));color:var(--white);font-family:"Noto Sans",sans-serif;font-weight:700;font-size:16px;line-height:40px;padding-left:25px;letter-spacing:.5px}
.section-head::before{content:"";position:absolute;left:0;top:-11px;border-right:11px solid var(--brown);border-top:11px solid transparent}
.catnav{left:114px;top:399px;width:219px;font-family:"Arimo",Arial,sans-serif}
.catnav .item{display:flex;align-items:center;height:25px;margin-bottom:4px;background:linear-gradient(90deg,#d8d8d8,#ececec);font-size:14px;color:#222;letter-spacing:.6px;padding-left:6px;position:relative}
.catnav .item svg.lead{margin-right:8px}
.catnav .item .chev{position:absolute;right:14px;top:8px;border-left:6px solid #222;border-top:5px solid transparent;border-bottom:5px solid transparent}
.catnav .item .down{position:absolute;right:12px;top:10px;border-top:6px solid #333;border-left:5px solid transparent;border-right:5px solid transparent}
.catnav .sub{background:var(--white);margin:2px 0 6px}
.catnav .sub a{display:block;height:27px;line-height:27px;font-size:11px;letter-spacing:.5px;color:#333;padding-left:29px;border-bottom:1px solid #eee;position:relative}
.catnav .sub a::before{content:"";position:absolute;left:14px;top:10px;border-left:5px solid #222;border-top:4px solid transparent;border-bottom:4px solid transparent}

.connect{left:114px;top:775px;width:219px;height:265px;background:var(--grey-panel)}
.social{position:absolute;left:28px;display:flex;align-items:center;gap:10px;font-family:"Noto Sans",sans-serif}
.social i{display:block;width:34px;height:34px;background:#3c5a99}
.social b{font-weight:400;font-size:21px;color:#2c4f8a;line-height:1}
.social small{display:block;font-size:14px;color:#2c4f8a}
.pay{position:absolute;display:flex;gap:14px}
.pay i{display:block;width:28px;height:18px;border-radius:2px}

/* hero */
.hero{left:333px;top:156px;width:764px;height:337px;background:linear-gradient(180deg,#c9b99b 0%,#a78f68 30%,#8d6548 65%,#b7a58a 100%)}
.hero-band{left:333px;top:389px;width:764px;height:86px;background:rgba(60,60,60,.62)}
.hero-title{left:349px;top:394px;font-family:"Noto Sans",sans-serif;font-size:35px;line-height:37px;color:var(--white)}
.hero-title em{font-style:normal;color:#e59a5c;font-weight:700}

/* welcome */
.welcome{left:345px;top:504px;width:506px}
.welcome h1{font-family:"Noto Sans",sans-serif;font-weight:400;font-size:22px;color:#444}
.welcome h1 strong{color:var(--accent-text)}
.welcome .lead{margin-top:8px;font-size:12px;line-height:16px;text-align:justify;color:#333}
.welcome h2{margin-top:18px;font-size:13px;font-weight:400;letter-spacing:1px;color:#222}
.welcome .body{margin-top:1px;font-size:12px;line-height:16px;letter-spacing:.8px;text-align:justify;color:#555}

/* products */
.product{top:752px;width:159px;height:283px;border:1px solid #e4e4e4;background:linear-gradient(#fff 60%,#f1f1f1);text-align:center}
.product .shot{width:140px;height:110px;margin:16px auto 0}
.product p{margin-top:16px;font-size:11px;line-height:18px;color:#333;padding:0 6px}
.product .price{position:absolute;left:0;right:0;top:210px;font-family:"Noto Sans",sans-serif;font-weight:300;font-size:27px;color:var(--accent-text)}
.product .addcart{position:absolute;left:36px;top:264px;width:96px;height:22px;border-radius:10px 10px 0 0;background:linear-gradient(#f4f4f4,#cfcfcf);font-family:"Noto Sans",sans-serif;font-size:13px;line-height:22px;color:#444}
.product .addcart::before,.product .addcart::after{content:"";position:absolute;bottom:-4px;width:16px;height:8px;border-radius:0 0 8px 8px;background:#333}
.product .addcart::before{left:-14px}
.product .addcart::after{right:-14px}

/* login panel */
.login{left:879px;top:525px;width:219px;height:515px;background:var(--grey-panel)}
.login h3{position:absolute;left:13px;top:9px;font-family:"Noto Sans",sans-serif;font-weight:400;font-size:19px;color:#444}
.login h3 strong{color:var(--accent-text)}
.login .note{position:absolute;left:13px;top:40px;width:200px;font-size:10px;line-height:14px;color:#333}
.login label{position:absolute;font-family:"Noto Sans",sans-serif;font-size:12px;color:#222}
.login .field{position:absolute;left:78px;width:130px;height:22px;border-radius:11px;background:#dcdcdc}
.login .forgot{position:absolute;left:25px;top:162px;font-family:"Noto Sans",sans-serif;font-size:12px;color:#333}
.login .btn{position:absolute;left:129px;top:182px;width:76px;height:26px;border-radius:5px;background:linear-gradient(#b06a36,#7a3c14);color:var(--white);font-family:"Noto Sans",sans-serif;font-size:15px;text-align:center;line-height:26px;box-shadow:0 1px 2px #777}
.promo{left:889px;top:753px;width:198px;height:277px;background:linear-gradient(160deg,#6f5a3e 0%,#4c4130 45%,#8a8a6a 75%,#c9c0a6 100%)}
.promo span{position:absolute;left:38px;top:8px;font-family:"Noto Sans",sans-serif;font-size:17px;line-height:25px;color:#f3f3e6}

/* footer */
.footer-rule{left:0;top:1057px;width:1200px;height:5px;background:#5a5a5a}
.footer{left:0;top:1062px;width:1200px;height:88px;background:var(--dark)}
.footnav{left:115px;top:1077px;font-size:12.5px;color:var(--white)}
.footnav span{margin:0 10px}
.copy{left:115px;top:1099px;font-size:12.5px;line-height:20px;color:var(--white)}
.follow{left:909px;top:1098px;display:flex;align-items:center;gap:10px;font-family:"Noto Sans",sans-serif;font-weight:700;font-size:13px;color:var(--red)}
.follow i{display:block;width:19px;height:19px;border-radius:2px}
</style>
</head>
<body>

<header>
  <div class="abs topbar"></div>
  <div class="abs topbar-rule"></div>
  <div class="abs subbar"></div>
  <nav class="abs account-links"><a href="#">My Account</a><span>|</span><a href="#">Order Tracking</a><span>|</span><a href="#">Wish List</a><span>|</span><a href="#">View Cart/Checkout</a></nav>
  <div class="abs search"><span>search..........</span>
    <svg width="20" height="18" viewBox="0 0 20 18"><circle cx="8" cy="7" r="5.5" fill="none" stroke="#222" stroke-width="2.2"/><line x1="12" y1="11" x2="18" y2="16" stroke="#222" stroke-width="3"/></svg>
  </div>
  <div class="abs phone">+(123) 555 0142</div>
  <div class="abs hours">Monday - Saturday: 7:30 am - 6:00 pm</div>
  <div class="abs brand-slot"></div>
  <div class="abs cart">
    <svg width="26" height="22" viewBox="0 0 26 22"><path d="M2 7h22l-3 13H5z" fill="none" stroke="#e08a3c" stroke-width="2"/><path d="M8 7l5-6 5 6" fill="none" stroke="#e08a3c" stroke-width="1.5"/><line x1="4" y1="12" x2="22" y2="12" stroke="#e08a3c" stroke-width="1.5"/><line x1="5" y1="16" x2="21" y2="16" stroke="#e08a3c" stroke-width="1.5"/></svg>Now in your cart <b>0 items</b>
  </div>

  <div class="abs navband"></div>
  <div class="abs navline" style="top:119px"></div>
  <div class="abs navline" style="top:152px"></div>
  <nav class="abs mainnav">
    <a href="#" class="active">Home</a><a href="#">About Us</a><a href="#">FAQ</a><a href="#">Recipes</a><a href="#">Locations</a><a href="#">Contact Us</a>
  </nav>
</header>

<aside>
  <div class="abs logo-area">
    <span class="mark"></span>
    <span class="name">Saveurs Du Matin</span>
  </div>
  <div class="abs section-head" style="top:352px">Quick Links:-</div>
  <nav class="abs catnav">
    <a class="item" href="#"><svg class="lead" width="14" height="14" viewBox="0 0 14 14"><path d="M2 12 Q2 4 9 4 L9 1 L13 6 L9 10 L9 7 Q5 7 2 12Z" fill="#c0622a"/></svg>Olive oils<i class="chev"></i></a>
    <a class="item" href="#"><svg class="lead" width="14" height="14" viewBox="0 0 14 14"><path d="M2 12 Q2 4 9 4 L9 1 L13 6 L9 10 L9 7 Q5 7 2 12Z" fill="#c0622a"/></svg>Balsamic Vinegars<i class="down"></i></a>
    <div class="sub">
      <a href="#">Vinegars and oils</a>
      <a href="#">Specialty salts</a>
      <a href="#">organic spices</a>
    </div>
    <a class="item" href="#"><svg class="lead" width="14" height="14" viewBox="0 0 14 14"><path d="M2 12 Q2 4 9 4 L9 1 L13 6 L9 10 L9 7 Q5 7 2 12Z" fill="#c0622a"/></svg>Misc<i class="chev"></i></a>
    <a class="item" href="#"><svg class="lead" width="14" height="14" viewBox="0 0 14 14"><path d="M2 12 Q2 4 9 4 L9 1 L13 6 L9 10 L9 7 Q5 7 2 12Z" fill="#c0622a"/></svg>Vinegars and oils<i class="chev"></i></a>
    <a class="item" href="#"><svg class="lead" width="14" height="14" viewBox="0 0 14 14"><path d="M2 12 Q2 4 9 4 L9 1 L13 6 L9 10 L9 7 Q5 7 2 12Z" fill="#c0622a"/></svg>Specialty salts<i class="chev"></i></a>
    <a class="item" href="#"><svg class="lead" width="14" height="14" viewBox="0 0 14 14"><path d="M2 12 Q2 4 9 4 L9 1 L13 6 L9 10 L9 7 Q5 7 2 12Z" fill="#c0622a"/></svg>organic spices<i class="chev"></i></a>
    <a class="item" href="#"><svg class="lead" width="14" height="14" viewBox="0 0 14 14"><path d="M2 12 Q2 4 9 4 L9 1 L13 6 L9 10 L9 7 Q5 7 2 12Z" fill="#c0622a"/></svg>Specialty Spices<i class="chev"></i></a>
    <a class="item" href="#"><svg class="lead" width="14" height="14" viewBox="0 0 14 14"><path d="M2 12 Q2 4 9 4 L9 1 L13 6 L9 10 L9 7 Q5 7 2 12Z" fill="#c0622a"/></svg>Kitchen Tools<i class="chev"></i></a>
  </nav>

  <div class="abs section-head" style="top:743px;height:32px;line-height:32px;padding-left:22px">Connect With Us</div>
  <div class="abs connect">
    <div class="social" style="top:24px"><i></i><span><small>Find us on</small><b>Friendlane</b></span></div>
    <div class="social" style="top:76px"><i style="background:#3fa9d8"></i><span><small>follow us on</small><b>Chirpwave</b></span></div>
    <div class="social" style="top:132px;left:36px"><b style="color:#222;font-size:24px">Linkora</b><i style="width:28px;height:28px;background:#1a73a8"></i></div>
    <div class="pay" style="left:18px;top:198px"><i style="background:#d9d9e6"></i><i style="background:#e9c7a5"></i><i style="background:#9fb8d6"></i><i style="background:#c9c9c9"></i></div>
    <div class="pay" style="left:36px;top:226px"><i style="background:#e2d0d0;height:12px"></i><i style="background:#d7d7d7;height:14px"></i><i style="background:#e8b4b4;height:12px"></i></div>
  </div>
</aside>

<main>
  <div class="abs hero" role="img" aria-label="Photo of a grocery aisle with shelves of spices and a shopper with a trolley"></div>
  <div class="abs hero-band"></div>
  <div class="abs hero-title"><em>Halloran's</em> Verdana<br>Estates Olive Oil</div>

  <section class="abs welcome">
    <h1>Welcome to <strong>Saveurs Du Matin</strong></h1>
    <p class="lead"><b>Lorem Ipsum is simply dummy text of the printing and typesetting industry. Lorem Ipsum has been the industry's standard</b> dummy text ever since the 1500s, when an unknown printer took a galley of type and scrambled it to make a type specimen book. It has survived not only five centuries, but also the leap into electronic typesetting, remaining essentially unchanged.</p>
    <h2>Our company presents the best traditions of classical business.</h2>
    <p class="body">Products such as concrete pigments, release agents and plasticisers are shipped concrete pigments, release agents and plasticisers are shipped world wide for the production of concrete, pre-cast concrete elements are shipped world wide for the production of concrete, pre-cast concrete blocks, etc.</p>
  </section>

  <article class="abs product" style="left:347px">
    <div class="shot" role="img" aria-label="Bottles of oil and vinegar with a bar of soap and lavender" style="background:radial-gradient(ellipse at 50% 70%,#e7a24e 0,#8a5a2a 35%,#fff 70%)"></div>
    <p>Contrary to popular belief, Lorem Ipsum is not simply random text.</p>
    <div class="price">$ 45.80</div>
    <a class="addcart" href="#">Add to Cart</a>
  </article>
  <article class="abs product" style="left:524px">
    <div class="shot" role="img" aria-label="Bottle of olive oil beside green olives and leaves" style="background:radial-gradient(ellipse at 50% 55%,#e6d23a 0,#7d9a3a 35%,#fff 70%)"></div>
    <p style="margin-top:10px">Contrary to popular belief, Lorem Ipsum is not simply random text.</p>
    <div class="price">$ 45.80</div>
    <a class="addcart" href="#">Add to Cart</a>
  </article>
  <article class="abs product" style="left:703px">
    <div class="shot" role="img" aria-label="Row of assorted organic oil bottles" style="background:radial-gradient(ellipse at 50% 55%,#c7c36a 0,#5b7a35 40%,#fff 72%)"></div>
    <p style="margin-top:12px">Contrary to popular belief, Lorem Ipsum is not simply random text.</p>
    <div class="price">$ 45.80</div>
    <a class="addcart" href="#">Add to Cart</a>
  </article>

  <section class="abs login">
    <h3>Already <strong>Costomers</strong></h3>
    <p class="note">When logged in you can access your account information at the link below.</p>
    <label style="left:12px;top:84px">Username :</label><span class="field" style="top:82px"></span>
    <label style="left:16px;top:118px">Password :</label><span class="field" style="top:116px"></span>
    <a class="forgot" href="#">Forgot password ?</a>
    <a class="btn" href="#">Login</a>
  </section>
  <div class="abs promo" role="img" aria-label="Bottle of green olive oil with a bowl of black olives and a dish of oil">
    <span>FRESHLY PRESSED<br>TUSCAN OLIVE OIL<br>ON SALE HERE</span>
  </div>
</main>

<footer>
  <div class="abs footer-rule"></div>
  <div class="abs footer"></div>
  <nav class="abs footnav"><a href="#">Home</a><span>|</span><a href="#">About Us</a><span>|</span><a href="#">FAQ</a><span>|</span><a href="#">Recipes</a><span>|</span><a href="#">Locations</a><span>|</span><a href="#">Contact Us</a></nav>
  <p class="abs copy">Copyright © saveurs du Matin All Right reseved 2012.<br>Privacy Policy | Terms Of Use</p>
  <div class="abs follow">Follow us: <i style="background:#3c5a99"></i><i style="background:#3fa9d8"></i><i style="background:#f08a24"></i></div>
</footer>

</body>
</html>
```